HollowPine Ventures Inc. Business Card Design

My business is custom renovations and homes.I would need to have a new business logo created to go along with my company name. The business card should be of a modern style as this is the market I am focused on. I would need my contact information and website posted on the card. I would also like to list a few of the tasks I conduct on the card (such as: Renovations, Additions, Repairs, New Homes, Design, Consultations). On the reverse of the card I currently have just my logo and my motto, "Shaping A Bold Path". However, I am open to completely changing everything as I am starting a new year and would like to excel further. Any new ideas and suggestions are always welcomed. Thank you.

Target Market(s)

Upscale residential and commercial renovations and builds

Industry/Entity Type

Business

Contact Information for Business Card

I would like the design to be able to be laser cut or burnt onto a wooden business card. I will be creating one option of cards for really loyal customers (wooden) and a second option for the everyday customer (paper).

Font styles to use
Other font styles liked:
• Calibri / anything of mordern taste

Colors
f37122
5c5c5c
474747
ffffff

Requirements
Must have
• I would like the colours of my business to be a sharp orange and grey. I believe this will symbolize a modern style. I am open to other suggestions if this is not suitable for the designers tastes. My contact info as follows:
• Will Marsh
• President
• HollowPine Ventures Inc.
• 555-214-3987
• will@hollowpineventures.example
• I would like my website (currently under construction) hollowpineventures.example on the card aswell.
Nice to have
• Along with a modern logo representing HollowPine, I would like something on the card besides the logo and contact information. Perhaps a small background design. I feel it may be nice to have my services listed on the card (in smaller font on the bottom) Renovations, Additions, Repairs, Design, Consultations.
Should not have
• The business card should not have too many different colors. Should not have rounded corners.

```html
<!DOCTYPE html>
<html lang="en">
<head>
<meta charset="utf-8">
<title>HollowPine Ventures Inc. — Business Card</title>
<link href="https://fonts.googleapis.com/css2?family=Open+Sans:wght@400;600;700&display=swap" rel="stylesheet">
<style>
  :root {
    --orange: #f37122;
    --grey: #5c5c5c;
    --grey-dark: #474747;
    --white: #ffffff;
    --backdrop: #2a2a2a;
  }
  * { box-sizing: border-box; margin: 0; padding: 0; }
  html, body {
    width: 1200px; height: 900px; overflow: hidden;
    background: var(--backdrop);
    font-family: "Open Sans", Calibri, sans-serif;
  }
  .card {
    position: absolute;
    width: 560px; height: 320px;
    background: var(--white);
    border-radius: 16px;
    overflow: hidden;
  }
  .card--front { left: 90px; top: 70px; }
  .card--back { left: 550px; top: 500px; }

  /* Front */
  .front-band-top {
    position: absolute; left: 0; top: 0; width: 100%; height: 34px;
    background: var(--orange);
  }
  .front-band-bottom {
    position: absolute; left: 0; bottom: 0; width: 100%; height: 52px;
    background: var(--orange);
  }
  .front-url {
    position: absolute; left: 0; right: 0; top: 14px;
    text-align: center; color: var(--white);
    font-size: 15px; letter-spacing: 3px;
  }
  .brand-mark {
    position: absolute; left: 0; right: 0; top: 96px;
    display: flex; justify-content: center; align-items: center; gap: 12px;
  }
  .brand-mark__square { width: 22px; height: 22px; background: var(--orange); }
  .brand-mark__name {
    color: var(--orange); font-weight: 700; font-size: 52px; line-height: 1;
    letter-spacing: -1px;
  }
  .front-company {
    position: absolute; left: 0; right: 0; top: 176px;
    text-align: center; color: var(--grey-dark);
    font-weight: 600; font-size: 22px; letter-spacing: 2.5px;
  }

  /* Back */
  .back-shape { position: absolute; left: 0; top: 0; }
  .back-mark {
    position: absolute; left: 30px; top: 44px;
    display: flex; align-items: center; gap: 8px;
  }
  .back-mark__square { width: 13px; height: 13px; background: var(--orange); }
  .back-mark__name {
    color: var(--orange); font-weight: 700; font-size: 27px; line-height: 1;
  }
  .back-company {
    position: absolute; left: 222px; top: 42px;
    color: var(--orange); font-size: 22px; letter-spacing: 1px; white-space: nowrap;
  }
  .back-company-rule {
    position: absolute; left: 222px; right: 0; top: 78px;
    height: 2px; background: var(--orange);
  }
  .contact-list {
    position: absolute; left: 250px; top: 102px; list-style: none;
  }
  .contact-list li {
    display: flex; align-items: center; gap: 10px;
    height: 27px; font-size: 14px; color: var(--grey-dark); letter-spacing: .3px;
    white-space: nowrap;
  }
  .contact-list svg { width: 17px; height: 17px; flex: none; }
  .contact-list .accent { color: var(--orange); }
  .person { position: absolute; left: 30px; top: 234px; }
  .person__name {
    font-weight: 700; font-size: 26px; line-height: 1; letter-spacing: .5px;
    color: var(--grey-dark); white-space: nowrap;
  }
  .person__name .surname { color: var(--orange); }
  .person__title {
    margin-top: 4px; font-size: 14px; letter-spacing: 3px; color: var(--grey-dark);
  }
  .services {
    position: absolute; right: 18px; top: 279px;
    color: var(--white); font-size: 11px; white-space: nowrap; text-align: right;
  }
</style>
</head>
<body>

<section class="card card--front" aria-label="Card front">
  <div class="front-band-top"></div>
  <div class="brand-mark">
    <span class="brand-mark__square"></span>
    <span class="brand-mark__name">HollowPine</span>
  </div>
  <p class="front-company">HollowPine Ventures Inc.</p>
  <div class="front-band-bottom">
    <p class="front-url">www.hollowpineventures.example</p>
  </div>
</section>

<section class="card card--back" aria-label="Card back">
  <svg class="back-shape" width="560" height="320" viewBox="0 0 560 320" aria-hidden="true">
    <polyline points="0,298 210,298 230,244 560,244" fill="none" stroke="#f37122" stroke-width="5"/>
    <polygon points="0,308 218,308 238,254 560,254 560,320 0,320" fill="#f37122"/>
  </svg>

  <div class="back-mark">
    <span class="back-mark__square"></span>
    <span class="back-mark__name">HollowPine</span>
  </div>
  <p class="back-company">HollowPine Ventures Inc.</p>
  <div class="back-company-rule"></div>

  <ul class="contact-list">
    <li>
      <svg viewBox="0 0 24 24" fill="none" stroke="#474747" stroke-width="1.6"><path d="M5 3h4l2 5-2.5 1.5a11 11 0 0 0 6 6L16 13l5 2v4a2 2 0 0 1-2 2A16 16 0 0 1 3 5a2 2 0 0 1 2-2z"/></svg>
      555-214-3987
    </li>
    <li>
      <svg viewBox="0 0 24 24" fill="none" stroke="#474747" stroke-width="1.6"><rect x="3" y="5" width="18" height="14"/><path d="M3 5l9 8 9-8"/></svg>
      will@hollowpineventures.example
    </li>
    <li>
      <svg viewBox="0 0 24 24" fill="none" stroke="#474747" stroke-width="1.6"><circle cx="12" cy="12" r="9"/><path d="M3 12h18M12 3c3 3 3 15 0 18M12 3c-3 3-3 15 0 18"/></svg>
      <span>www.<span class="accent">hollowpineventures</span>.example</span>
    </li>
  </ul>

  <div class="person">
    <p class="person__name">WILL <span class="surname">MARSH</span></p>
    <p class="person__title">PRESIDENT</p>
  </div>

  <p class="services">Renovations | Additions | Repairs | Design | Consultations</p>
</section>

</body>
</html>
```